Business cards and logo for kitchen and bath remodeling company

We want an elegant card but that calls attention something unique and when people see it they remember us. A log that we can use for our own. We are a kitchen and bathroom remodeling company. We are 3 partners staring the company we are located in seattle washington usa. We try to give the best experience and luxury look in our projects and we are looking to show that in our cards. I added a sample of a card I really like. I like the black and gold look but gray blue or green in a metallic look would look nice. I'm open to any color.

Target Market(s)

Home owners.

Industry/Entity Type

Construction

Contact Information for Business Card

Larchmont and Vey builders

Colors

Designer to choose colors to be used in the design.

Requirements
Must have
• Make a Logo
• Logo to be unique
• Name of company larchmont and vey builders
Nice to have
• Have a good color scheme
• Front design to connect with back of card

```html
<!DOCTYPE html>
<html lang="en">
<head>
<meta charset="utf-8">
<title>Larchmont &amp; Vey Builders — Business Card</title>
<link rel="stylesheet" href="https://fonts.googleapis.com/css2?family=Montserrat:wght@400;500;600&display=swap">
<style>
  :root {
    --bg: #e9ecec;
    --card-dark: #2a2b2f;
    --card-light: #ececee;
    --gold: #d9a000;
    --white: #ffffff;
    --ink: #2a2b2f;
    --muted: #4a4b50;
  }
  * { margin: 0; padding: 0; box-sizing: border-box; }
  html, body {
    width: 1200px; height: 900px; overflow: hidden;
    background: var(--bg);
    font-family: "Montserrat", Arial, sans-serif;
  }
  .sheet {
    position: relative; width: 1200px; height: 900px;
    display: flex; flex-direction: column; align-items: center; justify-content: center; gap: 40px;
  }
  .card {
    position: relative; width: 700px; height: 400px;
    box-shadow: 0 6px 18px rgba(0,0,0,0.12);
    display: flex; flex-direction: column; align-items: center;
  }
  .card--front { background: var(--card-dark); color: var(--white); }
  .card--back { background: var(--card-light); color: var(--ink); justify-content: center; }

  .brand {
    display: flex; align-items: center; gap: 16px;
    font-weight: 600; font-size: 38px; letter-spacing: 0.5px;
  }
  .brand__dot { width: 30px; height: 30px; border-radius: 50%; background: var(--gold); flex: none; }
  .card--front .brand { margin-top: 92px; color: var(--white); }
  .card--back .brand { color: var(--gold); }
  .card--back .brand__dot { background: var(--ink); }

  .details {
    position: absolute; left: 50px; right: 50px; bottom: 70px;
    font-weight: 400; font-size: 17px; letter-spacing: 0.3px;
  }
  .details__row { display: flex; align-items: center; gap: 14px; white-space: nowrap; }
  .details__sep { color: var(--gold); font-size: 22px; line-height: 1; }
  .details__rule { height: 2px; background: var(--gold); margin: 14px 0 14px 0; }
  .details__row--contact { font-size: 15px; padding-left: 30px; }

  .location {
    margin-top: 44px; font-size: 14px; font-weight: 500; letter-spacing: 1px; color: var(--muted);
  }
</style>
</head>
<body>
  <main class="sheet">
    <section class="card card--front" aria-label="Card front">
      <div class="brand">
        <span class="brand__dot"></span>
        <span class="brand__name">Larchmont &amp; Vey Builders</span>
      </div>
      <div class="details">
        <div class="details__row">
          <span>Larchmont &amp; Vey</span>
          <span class="details__sep">|</span>
          <span>Marisol Devereaux</span>
          <span class="details__sep">|</span>
          <span>CEO &amp; Founder</span>
        </div>
        <div class="details__rule"></div>
        <div class="details__row details__row--contact">
          <span>206 5550147</span>
          <span class="details__sep">|</span>
          <span>info.larchmontvey.com</span>
          <span class="details__sep">|</span>
          <span>www.larchmontvey.com</span>
        </div>
      </div>
    </section>

    <section class="card card--back" aria-label="Card back">
      <div class="brand">
        <span class="brand__dot"></span>
        <span class="brand__name">Larchmont &amp; Vey Builders</span>
      </div>
      <p class="location">Seattle Washington USA</p>
    </section>
  </main>
</body>
</html>
```